Pelarix PowerPoint Theme/Template

I want to be able to put together presentations that have a cohesive look and work with my current branding on my website (www.pelarix.com) and social media (#pelarixskincare).

```html
<!DOCTYPE html>
<html lang="en">
<head>
<meta charset="utf-8">
<title>Pelarix – Six Point Overview</title>
<link rel="stylesheet" href="https://fonts.googleapis.com/css2?family=Carlito:wght@400;700&display=swap">
<style>
  :root {
    --brown: #9b5a2b;
    --brown-title: #a0602d;
    --sand: #e6c3a2;
    --sand-deep: #dba878;
    --rule: #ebcfb4;
    --paper: #ffffff;
    --hex-text: #ffffff;
  }
  * { box-sizing: border-box; margin: 0; padding: 0; }
  html, body { width: 1200px; height: 676px; overflow: hidden; background: var(--paper); }
  body { font-family: "Carlito", "Calibri", Arial, sans-serif; color: var(--brown); }
  .slide { position: relative; width: 1200px; height: 676px; overflow: hidden; background: var(--paper); }

  .brand-line { position: absolute; left: 11px; top: 10px; font-size: 13px; font-weight: 700; color: var(--brown); }
  .brand-rule { position: absolute; left: 187px; top: 17px; width: 456px; height: 4px; background: var(--brown); }

  .slide-title { position: absolute; left: 0; right: 0; top: 56px; text-align: center; font-size: 40px; font-weight: 700; color: var(--brown-title); letter-spacing: 0.2px; }
  .title-rule { position: absolute; left: 37px; top: 103px; width: 1126px; height: 1px; background: var(--rule); }

  .hex-cluster { position: absolute; left: 0; top: 0; width: 1200px; height: 676px; }
  .hex { fill: var(--sand); }
  .hex-core { fill: var(--sand-deep); }
  .hex-label { fill: var(--hex-text); font-family: "Carlito", "Calibri", Arial, sans-serif; font-size: 46px; text-anchor: middle; dominant-baseline: central; }
  .hex-label.core { font-size: 56px; }

  .point { position: absolute; height: 50px; width: 1200px; left: 0; }
  .point-tag { position: absolute; top: 0; width: 99px; height: 50px; background: var(--sand); color: var(--brown); font-size: 13.5px; font-weight: 700; display: flex; align-items: center; justify-content: center; }
  .point-text { position: absolute; top: -5px; font-size: 13.5px; line-height: 19px; width: 336px; }
  .point-text h3 { font-size: 13.5px; font-weight: 700; line-height: 19px; }
  .point-text p { font-weight: 400; }

  .point.left .point-tag { left: 668px; border-radius: 10px 0 0 10px; }
  .point.left .point-text { left: 786px; text-align: left; }
  .point.right .point-tag { left: 1013px; border-radius: 0 10px 10px 0; }
  .point.right .point-text { left: 661px; text-align: right; }

  .footer-rule { position: absolute; left: 596px; top: 654px; width: 456px; height: 4px; background: var(--brown); }
  .tagline { position: absolute; left: 1071px; top: 647px; font-size: 13.5px; color: var(--brown); }
</style>
</head>
<body>
<main class="slide">
  <header>
    <div class="brand-line">Pelarix by dr. Mara Lindqvist</div>
    <div class="brand-rule"></div>
    <h1 class="slide-title">TITLE GOES HERE</h1>
    <div class="title-rule"></div>
  </header>

  <svg class="hex-cluster" viewBox="0 0 1300 732" aria-hidden="false">
    <polygon class="hex" points="233,227 270,144 390,144 426,227 390,311 270,311"/>
    <polygon class="hex" points="78,317 116,234 234,234 272,317 234,400 116,400"/>
    <polygon class="hex" points="390,317 428,233 546,233 584,317 546,400 428,400"/>
    <polygon class="hex" points="82,492 120,409 238,409 276,492 238,576 120,576"/>
    <polygon class="hex" points="390,492 428,409 546,409 584,492 546,576 428,576"/>
    <polygon class="hex" points="237,583 275,500 392,500 430,583 392,667 275,667"/>
    <polygon class="hex-core" points="214,405 268,311 394,311 448,405 394,500 268,500"/>
    <text class="hex-label" x="329" y="227">[Text]</text>
    <text class="hex-label" x="175" y="317">[Text]</text>
    <text class="hex-label" x="487" y="317">[Text]</text>
    <text class="hex-label" x="178" y="492">[Text]</text>
    <text class="hex-label" x="487" y="492">[Text]</text>
    <text class="hex-label" x="333" y="583">[Text]</text>
    <text class="hex-label core" x="331" y="405">[Text]</text>
  </svg>

  <section class="points">
    <div class="point left" style="top:156px">
      <div class="point-tag">One 01</div>
      <div class="point-text"><h3>Title Text Goes Here</h3><p>Lorem Ipsum is simply dummy text of the printing and typesetting industry.</p></div>
    </div>
    <div class="point right" style="top:236px">
      <div class="point-text"><h3>Title Text Goes Here</h3><p>Lorem Ipsum is simply dummy text of the printing and typesetting industry.</p></div>
      <div class="point-tag">Two 02</div>
    </div>
    <div class="point left" style="top:317px">
      <div class="point-tag">Three 03</div>
      <div class="point-text"><h3>Title Text Goes Here</h3><p>Lorem Ipsum is simply dummy text of the printing and typesetting industry.</p></div>
    </div>
    <div class="point right" style="top:396px">
      <div class="point-text"><h3>Title Text Goes Here</h3><p>Lorem Ipsum is simply dummy text of the printing and typesetting industry.</p></div>
      <div class="point-tag">Four 04</div>
    </div>
    <div class="point left" style="top:474px">
      <div class="point-tag">Five 05</div>
      <div class="point-text"><h3>Title Text Goes Here</h3><p>Lorem Ipsum is simply dummy text of the printing and typesetting industry.</p></div>
    </div>
    <div class="point right" style="top:554px">
      <div class="point-text"><h3>Title Text Goes Here</h3><p>Lorem Ipsum is simply dummy text of the printing and typesetting industry.</p></div>
      <div class="point-tag">Six 06</div>
    </div>
  </section>

  <footer>
    <div class="footer-rule"></div>
    <div class="tagline">Love for your skin</div>
  </footer>
</main>
</body>
</html>
```